New SKINCARE Label Design Project

Check out our website www.morleneglow.com. We offer a few products that are all natural, from drinks to skincare. We have new packaging for the "Dewbrin Balm" and need a new label design. We'd like out of the box thinking, but it should fit the existing concept. The product label should contain cool words, can be creative and should contain ingredients as this is a regulation.

I have added some examples of what we’d like. Please base your design on this.

Target Market(s)

skincare, cosmetics, natural, cool, young

Industry/Entity Type

Skin Care Product

Requirements
Must have
• Label must fit the existing concept, but should be out of the box, potentially using unexpected colors... Clean design, clean fonts, very professional, but playful at the same time, can maybe include cartoons, stars,...
Nice to have
• Out of the box thinking, we'd like to stand out from all other brands by label design, it should catch the eye and interest people to buy our product.

```html
<!DOCTYPE html>
<html lang="en">
<head>
<meta charset="utf-8">
<title>Dewbrin Balm – Label</title>
<link href="https://fonts.googleapis.com/css2?family=Fira+Sans:wght@600;700&family=Arimo:wght@400;700&display=swap" rel="stylesheet">
<style>
  :root {
    --canvas-bg: #f3f0e6;
    --label-white: #ffffff;
    --ink: #3a3439;
    --taupe: #6d6560;
    --taupe-light: #827a75;
    --silver: #b9b4b1;
    --brand-dark: #1e1b1c;
    --accent: #f08a6c;
    --text-on-dark: #ffffff;
    --text-soft: rgba(255,255,255,0.82);
  }
  * { margin: 0; padding: 0; box-sizing: border-box; }
  html, body { width: 1200px; height: 1200px; overflow: hidden; }
  body {
    background: var(--canvas-bg);
    display: flex;
    align-items: center;
    justify-content: center;
  }
  .label {
    position: relative;
    width: 460px;
    height: 1040px;
    background: var(--label-white);
    overflow: hidden;
    box-shadow: 0 2px 10px rgba(0,0,0,0.06);
  }
  .brand {
    position: absolute;
    top: 140px;
    left: 0; right: 0;
    text-align: center;
  }
  .brand-row {
    display: inline-flex;
    align-items: center;
    gap: 10px;
  }
  .brand-dot {
    width: 14px;
    height: 14px;
    border-radius: 50%;
    background: var(--accent);
  }
  .brand-name {
    font-family: "Fira Sans", sans-serif;
    font-weight: 600;
    font-size: 52px;
    color: var(--brand-dark);
    letter-spacing: 1px;
    line-height: 1;
  }
  .brand-tagline {
    margin-top: 8px;
    font-family: "Arimo", sans-serif;
    font-size: 9px;
    letter-spacing: 1.5px;
    color: var(--brand-dark);
  }
  .title-block {
    position: absolute;
    top: 300px;
    left: 52px; right: 52px;
    border-top: 1.5px solid var(--ink);
    border-bottom: 1.5px solid var(--ink);
    padding: 10px 0 8px;
    text-align: center;
  }
  .product-name {
    font-family: "Fira Sans", sans-serif;
    font-weight: 700;
    font-size: 60px;
    line-height: 1.02;
    color: var(--ink);
    letter-spacing: 2px;
  }
  .swoosh {
    position: absolute;
    left: 0;
    top: 480px;
    width: 460px;
    height: 560px;
  }
  .illustration {
    position: absolute;
    top: 640px;
    left: 110px;
    width: 240px;
    height: 240px;
    border-radius: 50%;
    background: radial-gradient(circle, rgba(255,255,255,0.07), rgba(255,255,255,0) 70%);
  }
  .claim {
    position: absolute;
    top: 715px;
    left: 0; right: 0;
    text-align: center;
    font-family: "Arimo", sans-serif;
    font-size: 21px;
    line-height: 1.4;
    color: var(--text-on-dark);
  }
  .claim-mark {
    display: block;
    width: 36px;
    height: 3px;
    margin: 12px auto 0;
    border-radius: 2px;
    background: var(--accent);
  }
  .ingredients {
    position: absolute;
    top: 840px;
    left: 70px; right: 70px;
    text-align: center;
    font-family: "Arimo", sans-serif;
    font-size: 11px;
    line-height: 1.5;
    color: var(--text-soft);
  }
  .ingredients strong {
    font-weight: 700;
    color: var(--text-on-dark);
  }
  .volume {
    position: absolute;
    top: 935px;
    left: 0; right: 0;
    text-align: center;
    font-family: "Arimo", sans-serif;
    font-size: 15px;
    color: var(--text-on-dark);
  }
</style>
</head>
<body>
  <main class="label">
    <header class="brand">
      <div class="brand-row">
        <span class="brand-dot"></span>
        <span class="brand-name">morlene</span>
      </div>
      <div class="brand-tagline">THE GLOW COMPANY</div>
    </header>

    <section class="title-block">
      <h1 class="product-name">DEWBRIN<br>BALM</h1>
    </section>

    <svg class="swoosh" viewBox="0 0 460 560" preserveAspectRatio="none" aria-hidden="true">
      <defs>
        <linearGradient id="taupe-fill" x1="0" y1="0" x2="1" y2="0">
          <stop offset="0" stop-color="#6d6560"/>
          <stop offset="0.6" stop-color="#827a75"/>
          <stop offset="1" stop-color="#6d6560"/>
        </linearGradient>
      </defs>
      <path d="M0 110 C120 40 300 30 460 10 L460 30 C300 50 140 70 0 140 Z" fill="#b9b4b1"/>
      <path d="M0 125 C130 70 300 55 460 40 L460 560 L0 560 Z" fill="url(#taupe-fill)"/>
    </svg>

    <div class="illustration" role="img" aria-label="Line drawing of a peony flower with leaves"></div>

    <p class="claim">Nourishes &amp;<br>Protects the Skin<span class="claim-mark"></span></p>

    <p class="ingredients"><strong>Ingredients:</strong> Aqua, Shea Butter, Glycerin, Jojoba Seed Oil, Aloe Leaf Juice, Cetearyl Alcohol, Tocopherol, Rose Flower Water.</p>

    <p class="volume">100 mL</p>
  </main>
</body>
</html>
```